Infographic on Creating Powerful Infographics

I would like to create an infographic the gives guidance on effective/best practices, for developing... infographics. There are a bunch of these out there, and I've borrowed and tweaked the content to fit our needs with in my brand. There are 7 tips or cells, so I'm thinking of creating illustrations (one for each tip) of a superhero (comic book style) . The illustrations would take queues from the said content for that tip (will attach an example to better explain). The final product would be PDF that I would give to vendors/agencies that are creating infographics for my company. You can use a font other than Muselle for the comic based subheads, something that will match or partner with the illustrations.

Attached is a very simple KLW infographic (KLW_BrandTop5_final.pdf) Use this a guide for the base art.

Also attached is a word doc of content, KLW brand guidelines, and an example infographic which is close to what I'm after - I think we can improve upon it. Better superhero(s) - less funky would improve the concept. The end product will need to be a bit more corporate.

Industry/Entity Type

It Company

Requirements
Must have
• Use our company color palette (will provide)
Use our corporate font (Muselle) - for the base text
Use our corporate logo
Final file .eps vector based

```html
<!DOCTYPE html>
<html lang="en">
<head>
<meta charset="utf-8">
<title>Creating Powerful Infographics – Seven Super Tips</title>
<link href="https://fonts.googleapis.com/css2?family=Arimo:wght@400;700&family=Lilita+One&display=swap" rel="stylesheet">
<style>
:root{
  --blue:#1a8ad6;
  --blue-bright:#2e9cf0;
  --blue-band:#5a9ee0;
  --blue-band-dark:#4b8fd4;
  --ink:#1b1b1b;
  --slate:#4a4a4a;
  --paper:#efefef;
  --stripe:#e6e6e6;
  --white:#ffffff;
  --note:#f7e24a;
}
*{box-sizing:border-box;margin:0;padding:0}
html,body{width:1200px;height:4523px;overflow:hidden}
body{background:var(--paper);font-family:"Arimo",Arial,sans-serif;color:var(--ink);position:relative}
.canvas{position:relative;width:1200px;height:4523px;overflow:hidden;
  background:repeating-linear-gradient(135deg,var(--paper) 0 40px,var(--stripe) 40px 80px)}
.abs{position:absolute}
.band{position:absolute;left:0;width:1200px;background:var(--blue-band)}
.band.dark{background:var(--blue-band-dark)}
.illus{position:absolute;border-radius:40px}
.title{position:absolute;left:0;width:1200px;text-align:center;font-family:"Lilita One",sans-serif;color:var(--blue);letter-spacing:2px;line-height:1}
.title.top{top:30px;font-size:62px}
.title.main{top:96px;font-size:96px}
.burst{position:absolute;left:690px;top:250px;width:260px;height:210px}
.burst-text{position:absolute;left:690px;top:300px;width:260px;text-align:center;color:var(--white);font-family:"Lilita One",sans-serif;line-height:1.1}
.burst-text .big{font-size:48px;display:block}
.burst-text .small{font-size:34px}
.burst-text .hl{color:var(--note)}
.tab{position:absolute;left:45px;height:72px;width:500px;background:var(--white);border-radius:0 36px 36px 0;
  display:flex;align-items:center;gap:18px;padding-left:30px;box-shadow:0 4px 0 rgba(0,0,0,.15)}
.tab-num{width:54px;height:54px;border-radius:50%;background:var(--ink);color:var(--white);
  font-weight:700;font-size:38px;display:flex;align-items:center;justify-content:center}
.tab-label{color:var(--blue);font-weight:700;font-size:44px}
.bubble{position:absolute;display:flex;align-items:center;justify-content:center;text-align:center;font-size:25px;line-height:1.2;padding:20px}
.bubble > span{display:block}
.bubble.blue{background:var(--blue-bright);color:var(--white);border-radius:50%}
.bubble.slate{background:var(--slate);color:var(--white);border-radius:50%}
.bubble.white{background:var(--white);color:var(--ink);border-radius:50%}
.bubble.black{background:var(--ink);color:var(--white);border-radius:46% 54% 40% 60%}
.box{position:absolute;font-size:25px;line-height:1.25;padding:16px 22px;box-shadow:4px 6px 0 rgba(0,0,0,.2)}
.box.white{background:var(--white);color:var(--ink)}
.box.black{background:var(--ink);color:var(--white)}
.box.blue{background:var(--blue-bright);color:var(--white)}
.box.slate{background:var(--slate);color:var(--white)}
.box.note{background:var(--note);color:var(--ink)}
.em{color:var(--blue);font-weight:700}
.strong{font-weight:700}
.lead{position:absolute;font-size:32px;color:var(--ink);line-height:1.1}
.lead .big{font-family:"Lilita One",sans-serif;color:var(--blue);font-size:66px}
.pie-word{position:absolute;left:290px;top:3035px;font-family:"Lilita One",sans-serif;color:var(--blue);font-size:76px;line-height:1}
.brand-chip{position:absolute;display:flex;align-items:center;gap:10px;font-size:26px;font-weight:700;color:var(--ink)}
.brand-chip i{display:block;width:26px;height:26px;background:var(--blue)}
.footer{position:absolute;left:0;top:4478px;width:1200px;height:45px;background:var(--white);font-size:18px;
  display:flex;align-items:center;padding-left:40px;color:var(--slate)}
</style>
</head>
<body>
<div class="canvas">

  <!-- Header -->
  <div class="title top">CREATING POWERFUL</div>
  <div class="title main">INFOGRAPHICS</div>
  <div class="illus" role="img" aria-label="Comic superhero in orange costume flexing an arm" style="left:330px;top:180px;width:280px;height:455px;background:linear-gradient(180deg,#f4a64a,#e9782a)"></div>
  <svg class="burst" viewBox="0 0 260 210" aria-hidden="true"><polygon fill="#1a8ad6" points="130,0 150,40 200,15 195,60 255,55 220,100 260,135 205,145 225,200 165,170 130,210 100,170 40,200 55,145 0,135 40,100 5,55 65,60 60,15 110,40"/></svg>
  <div class="burst-text"><span class="big">SEVEN</span><span class="small">SUPER <span class="hl">TIPS</span></span></div>
  <div class="illus" role="img" aria-label="Blue lightbulb with an S emblem" style="left:960px;top:450px;width:210px;height:270px;background:radial-gradient(circle,#2e9cf0,#1a6fb8)"></div>

  <!-- 1 Story -->
  <div class="tab" style="top:648px"><span class="tab-num">1</span><span class="tab-label">Story</span></div>
  <div class="lead" style="left:150px;top:735px">What's the Big <span class="big">Idea?</span></div>
  <div class="illus" role="img" aria-label="Caped superhero with arms crossed" style="left:520px;top:700px;width:460px;height:445px;background:linear-gradient(160deg,#e05a3a,#3b7fc4 60%,#2e5f96)"></div>
  <div class="bubble blue" style="left:120px;top:860px;width:260px;height:170px"><span>Connect the dots to <span class="strong">share</span> your story.</span></div>
  <div class="bubble slate" style="left:405px;top:960px;width:260px;height:150px"><span>Help educate or inspire your target audience.</span></div>
  <div class="bubble white" style="left:780px;top:920px;width:240px;height:120px;color:var(--slate)"><span>structure to your <span class="em">story.</span></span></div>
  <div class="box white" style="left:760px;top:1055px;width:210px;font-size:20px;padding:8px 14px;color:var(--blue);font-weight:700;box-shadow:none;border-radius:20px">Use visuals to support and</div>
  <svg class="abs" style="left:985px;top:1040px" width="110" height="70" viewBox="0 0 110 70" aria-hidden="true">
    <g fill="#1b1b1b"><circle cx="30" cy="40" r="18"/><g stroke="#1b1b1b" stroke-width="8"><line x1="30" y1="12" x2="30" y2="68"/><line x1="2" y1="40" x2="58" y2="40"/><line x1="10" y1="20" x2="50" y2="60"/><line x1="50" y1="20" x2="10" y2="60"/></g></g>
    <g fill="#1a8ad6"><circle cx="85" cy="25" r="13"/><g stroke="#1a8ad6" stroke-width="6"><line x1="85" y1="4" x2="85" y2="46"/><line x1="64" y1="25" x2="106" y2="25"/><line x1="70" y1="10" x2="100" y2="40"/><line x1="100" y1="10" x2="70" y2="40"/></g></g>
  </svg>

  <!-- 2 Style -->
  <div class="tab" style="top:1160px"><span class="tab-num">2</span><span class="tab-label">Style</span></div>
  <div class="box blue" style="left:210px;top:1260px;width:430px;box-shadow:none">A well-styled <span class="strong">Infographic</span> is...</div>
  <div class="band" style="top:1450px;height:800px"></div>
  <div class="band dark" style="top:1770px;height:30px;opacity:.5"></div>
  <div class="illus" role="img" aria-label="Masked superhero face" style="left:460px;top:1395px;width:140px;height:170px;background:linear-gradient(180deg,#f5a04a,#f3c79a)"></div>
  <div class="bubble blue" style="left:110px;top:1490px;width:340px;height:200px;font-size:23px"><span>Hierarchical - use size, color and images to make important information pop</span></div>
  <div class="box slate" style="left:690px;top:1450px;width:270px;font-size:23px">Visually appealing</div>
  <div class="box blue" style="left:700px;top:1535px;width:310px;font-size:23px;background:var(--blue)">Balanced and consistent</div>
  <div class="box white" style="left:650px;top:1620px;width:490px;font-size:23px">Digestible – bite size chunks of information</div>

  <!-- 3 Simplicity -->
  <div class="tab" style="top:1760px"><span class="tab-num">3</span><span class="tab-label">Simplicity</span></div>
  <div class="bubble black" style="left:70px;top:1855px;width:290px;height:170px;font-size:22px"><span>Be consistent and limit the number of fonts you use (try and use Halden Sans or Muselle)</span></div>
  <div class="box white" style="left:400px;top:1840px;width:400px;font-size:27px">White space is your <span class="em">friend!</span></div>
  <div class="illus" role="img" aria-label="Framed photograph icon labelled images" style="left:895px;top:1820px;width:95px;height:100px;border-radius:4px;background:linear-gradient(135deg,#f0c070,#c9553a)"></div>
  <div class="box white" style="left:810px;top:1955px;width:330px;font-size:23px;box-shadow:none">Stick to <span class="strong">one style</span> for images /graphics/photos.</div>
  <div class="box white" style="left:345px;top:2040px;width:220px;font-size:23px;text-align:center;border-radius:40px">Establish a flow and connection from <span class="em">section to section.</span></div>
  <svg class="abs" style="left:575px;top:2080px" width="80" height="80" viewBox="0 0 80 80" aria-hidden="true"><circle cx="40" cy="40" r="22" fill="#1b1b1b"/><g stroke="#1b1b1b" stroke-width="10"><line x1="40" y1="2" x2="40" y2="78"/><line x1="2" y1="40" x2="78" y2="40"/><line x1="13" y1="13" x2="67" y2="67"/><line x1="67" y1="13" x2="13" y2="67"/></g><circle cx="40" cy="40" r="8" fill="#5a9ee0"/></svg>
  <div class="box white" style="left:715px;top:2120px;width:290px;font-size:23px;border-radius:40px">Restrict your color palette (use KLW colors) and the density of the graphic.</div>
  <svg class="abs" style="left:880px;top:2265px" width="170" height="80" viewBox="0 0 170 80" aria-hidden="true"><rect x="0" y="10" width="50" height="65" fill="#e6e6e6" transform="rotate(-8 25 40)"/><rect x="40" y="8" width="45" height="65" fill="#d63a2e" transform="rotate(-4 60 40)"/><rect x="80" y="6" width="45" height="65" fill="#2e9cf0"/><rect x="118" y="8" width="45" height="65" fill="#3fae49" transform="rotate(6 140 40)"/></svg>

  <!-- 4 Size and Shape -->
  <div class="tab" style="top:2220px;width:560px"><span class="tab-num">4</span><span class="tab-label">Size and Shape</span></div>
  <div class="box white" style="left:360px;top:2395px;width:400px;font-size:24px;box-shadow:none">The size should fit the <span class="em">medium</span></div>
  <svg class="abs" style="left:175px;top:2330px" width="70" height="110" viewBox="0 0 70 110" aria-hidden="true"><rect x="5" y="5" width="60" height="100" rx="10" fill="#1b1b1b"/><rect x="14" y="20" width="42" height="55" fill="#ffffff"/></svg>
  <div class="band" style="top:2460px;height:370px"></div>
  <svg class="abs" style="left:485px;top:2460px" width="90" height="120" viewBox="0 0 90 120" aria-hidden="true"><rect x="5" y="5" width="80" height="110" rx="10" fill="#1b1b1b"/><rect x="14" y="16" width="62" height="84" fill="#ffffff"/></svg>
  <div class="bubble blue" style="left:250px;top:2505px;width:270px;height:150px;font-size:23px"><span>Take into account viewability on tablets and mobile devices.</span></div>
  <div class="box black" style="left:510px;top:2600px;width:230px;height:170px;font-size:23px;transform:rotate(-10deg)">Use compressed JPEG images to reduce load-time.</div>
  <svg class="abs" style="left:625px;top:2720px" width="70" height="70" viewBox="0 0 70 70" aria-hidden="true"><circle cx="35" cy="35" r="30" fill="#fff" stroke="#bbb" stroke-width="5"/><text x="35" y="41" text-anchor="middle" font-family="Arimo,Arial,sans-serif" font-size="17" font-weight="700" fill="#1b1b1b">23%</text></svg>
  <div class="bubble blue" style="left:790px;top:2495px;width:320px;height:180px;font-size:22px"><span>Ideal horizontal width is 735 pixels – 5000 pixels high. If it's too long you will lose attention.</span></div>

  <!-- 5 Stats -->
  <div class="tab" style="top:2895px"><span class="tab-num">5</span><span class="tab-label">Stats</span></div>
  <div class="lead" style="left:270px;top:2995px">Its not about the</div>
  <div class="pie-word">Pie chart</div>
  <svg class="abs" style="left:610px;top:2955px" width="190" height="190" viewBox="0 0 200 200" aria-hidden="true"><circle cx="100" cy="100" r="95" fill="#1b1b1b"/><path d="M100 100 L100 5 A95 95 0 0 1 195 100 Z" fill="#1a8ad6"/><path d="M100 100 L195 100 A95 95 0 0 1 120 193 Z" fill="#ffffff"/></svg>
  <div class="bubble black" style="left:140px;top:3125px;width:320px;height:170px;font-size:22px;text-align:left"><span><span class="strong" style="font-size:34px">53%</span> of the most-shared infographics do not actually contain data visualization.</span></div>
  <svg class="abs" style="left:810px;top:2920px" width="270" height="390" viewBox="0 0 270 390" aria-hidden="true"><path d="M0 0 H270 V300 L135 390 L0 300 Z" fill="#1a8ad6"/></svg>
  <div class="abs" style="left:810px;top:2940px;width:270px;text-align:center;color:var(--white);font-size:26px;line-height:1.35"><span class="strong" style="font-size:32px">STATS</span><br>should be<br><span class="strong">current,<br>topical,<br>factual,<br>helpful,<br>and reliable.</span></div>
  <div class="box blue" style="left:300px;top:3315px;width:630px;font-size:23px;font-style:italic">Infographic posts are shared more readily than traditional posts on <span class="strong">Chirpline, Linkora and other social sites.</span></div>
  <div class="brand-chip" style="left:620px;top:3428px"><i></i>Chirpline</div>
  <div class="brand-chip" style="left:790px;top:3428px"><i></i>Linkora</div>

  <!-- 6 Source -->
  <div class="tab" style="top:3480px"><span class="tab-num">6</span><span class="tab-label">Source</span></div>
  <div class="band" style="top:3560px;height:320px"></div>
  <div class="box white" style="left:370px;top:3575px;width:500px;font-size:25px;box-shadow:none">Give your infographic <span class="em">credibility</span></div>
  <svg class="abs" style="left:160px;top:3670px" width="130" height="130" viewBox="0 0 130 130" aria-hidden="true"><g fill="none" stroke="#ffffff" stroke-width="6"><circle cx="65" cy="65" r="58"/><ellipse cx="65" cy="65" rx="25" ry="58"/><line x1="7" y1="65" x2="123" y2="65"/><path d="M15 35 H115 M15 95 H115"/></g></svg>
  <div class="box white" style="left:360px;top:3690px;width:160px;height:130px;font-size:23px;font-style:italic">Confirm your facts.</div>
  <div class="box black" style="left:530px;top:3730px;width:170px;height:140px;font-size:23px;font-style:italic;transform:rotate(-6deg)">Confirm your facts again.</div>
  <svg class="abs" style="left:715px;top:3765px" width="80" height="80" viewBox="0 0 80 80" aria-hidden="true"><rect x="10" y="12" width="60" height="8" fill="#1b1b1b"/><path d="M16 24 H64 L58 76 H22 Z" fill="#1a8ad6"/><g stroke="#fff" stroke-width="3"><line x1="32" y1="32" x2="33" y2="68"/><line x1="48" y1="32" x2="47" y2="68"/></g></svg>
  <div class="box note" style="left:850px;top:3660px;width:180px;height:160px;font-size:23px;transform:rotate(4deg);padding-top:40px">Use reputable sources.</div>

  <!-- 7 Sign and Share -->
  <div class="tab" style="top:3890px;width:560px"><span class="tab-num">7</span><span class="tab-label">Sign and Share</span></div>
  <div class="band" style="top:3965px;height:513px"></div>
  <div class="box white" style="left:350px;top:4000px;width:430px;font-size:24px;box-shadow:none">Optimize and spread the <span class="em">love</span></div>
  <div class="bubble blue" style="left:790px;top:3945px;width:310px;height:120px;font-size:23px"><span>Don't forget links to <span class="strong">social accounts.</span></span></div>
  <div class="bubble blue" style="left:160px;top:4085px;width:270px;height:130px;font-size:23px"><span>Include source info and URL.</span></div>
  <div class="illus" role="img" aria-label="Orange-suited superhero standing with fists on hips" style="left:500px;top:4075px;width:220px;height:390px;background:linear-gradient(180deg,#f4a64a,#e9782a)"></div>
  <div class="box white" style="left:770px;top:4160px;width:320px;font-size:23px">Get approval from <span class="em">KLW Brand</span> Review before finalizing.</div>
  <div class="box black" style="left:265px;top:4245px;width:215px;font-size:22px;text-align:center;transform:rotate(-5deg)">Must include the <span class="strong">PROPER NORVANE</span> and KLW Data Systems <span class="strong">LOGOS.</span></div>

  <div class="footer">© KLW Data Systems Corporation 2014. All rights reserved. NORVANE is a trademark or registered trademark of Norvane, Ltd.</div>
</div>
</body>
</html>
```